Dredging Contractors, we run amphibious walking dredges cleaning up waterways, mines etc

We need an updated web design for our company based in Australia.
We have 20t "Walking" amphibious excavators that service mining companies and governments, cleaning up waterways and pond systems.
We would like to see designs that reflect our cutting edge marine / technology that appeals to our engineering / civil / mining clients. As well as providing benefits by cleaning up our marine waterways.
We have an existing web page at www.korvellmarine.com.au

Target Market(s)

Mining companies, engineers, council civil engineers, developers, waterways engineers

Industry/Entity Type

It Company

Requirements
Must have
• Logo, contact details, Photos of equipment page (Gallery), quotation page, Contact page, list of capabilities page (Products and services),

```html
<!DOCTYPE html>
<html lang="en">
<head>
<meta charset="utf-8">
<title>Korvell Marine – Amphibious Dredging</title>
<link rel="stylesheet" href="https://fonts.googleapis.com/css2?family=Ubuntu:wght@300;400;500;700&display=swap">
<style>
:root{
  --teal:#1a9c98;
  --teal-dark:#12807d;
  --teal-light:#23aea9;
  --ink:#2b2b2b;
  --text:#555b60;
  --muted:#8a9499;
  --link:#1d6f8c;
  --bg-soft:#eef5f9;
  --card-border:#dbe7ee;
  --footer:#2f2f2f;
  --footer-text:#f0f0f0;
  --footer-muted:#8c8c8c;
}
*{margin:0;padding:0;box-sizing:border-box}
html,body{width:851px;height:1200px;overflow:hidden}
body{position:relative;font-family:'Ubuntu',sans-serif;background:#fff;color:var(--text)}
.top-band{position:absolute;left:0;top:0;width:851px;height:478px;background:linear-gradient(#fff 0,var(--bg-soft) 100%)}
.utility-nav{position:absolute;right:43px;top:15px;font-size:11.5px;color:var(--link)}
.utility-nav span{margin:0 6px;color:#666}
.brand{position:absolute;left:35px;top:30px;display:flex;align-items:center;gap:10px}
.brand-mark{width:64px;height:64px;border-radius:50%;background:var(--teal)}
.brand-name{font-size:27px;font-weight:700;color:var(--ink);line-height:27px;letter-spacing:.5px}
.search{position:absolute;left:620px;top:69px;width:194px;height:25px;border:1px solid #c9d2d6;background:#fff;font-size:10px;font-style:italic;color:#999;padding:7px 10px}
.search svg{position:absolute;right:7px;top:5px}
.main-nav{position:absolute;left:30px;top:110px;width:791px;height:50px;background:linear-gradient(var(--teal-light),var(--teal-dark));display:flex;border-radius:2px 2px 0 0}
.main-nav a{color:#fff;font-size:11.5px;line-height:15px;padding:0 10px;display:flex;align-items:center;border-right:1px solid rgba(255,255,255,.25);text-decoration:none}
.main-nav a:last-child{border-right:0}
.hero{position:absolute;left:30px;top:160px;width:791px;height:294px;background:#fff;box-shadow:0 2px 4px rgba(0,0,0,.08)}
.hero-photo{position:absolute;left:8px;top:6px;width:775px;height:280px;background:linear-gradient(170deg,#4a8fd8 0%,#7fb4e8 45%,#3e7a3f 70%,#2c6a3c 100%)}
.hero-arrows{position:absolute;right:20px;bottom:14px}
.card-arrow{position:absolute;top:572px;width:28px;height:28px;border-radius:50%;background:#e2eef5;display:flex;align-items:center;justify-content:center}
.card{position:absolute;top:494px;width:171px;height:192px;border:1px solid var(--card-border);background:linear-gradient(#fff 60%,#eef5f9);border-radius:2px}
.card-photo{position:absolute;left:12px;top:12px;width:148px;height:92px}
.card h3{position:absolute;left:13px;top:113px;font-size:14.5px;font-weight:400;color:var(--link)}
.card p{position:absolute;left:13px;top:135px;width:150px;font-size:9.5px;font-weight:300;line-height:16px;color:var(--muted)}
.why{position:absolute;left:44px;top:728px;width:500px}
.why h2{font-size:20px;font-weight:400;color:var(--ink)}
.why .lead{margin-top:12px;font-size:11.5px;color:var(--ink)}
.why .body{margin-top:12px;font-size:9.8px;font-weight:300;line-height:15.5px;color:#444}
.checklist{list-style:none;margin-top:17px}
.checklist li{position:relative;padding-left:21px;font-size:9.8px;font-weight:300;line-height:15.5px;color:var(--link);margin-bottom:11.5px}
.checklist svg{position:absolute;left:4px;top:3px}
.gallery{position:absolute;left:564px;top:725px;width:257px;height:323px;border:1px solid #e0e6e9;background:#fff}
.gallery-head{height:43px;background:linear-gradient(#444,#1f1f1f);color:#fff;font-size:17px;padding:13px 18px}
.thumb{position:absolute;width:72px;height:62px}
.btn{position:absolute;left:146px;top:282px;width:98px;height:24px;background:var(--teal);color:#fff;font-size:9.5px;text-align:center;line-height:24px;border-radius:2px}
.footer{position:absolute;left:0;top:1090px;width:851px;height:110px;background:var(--footer)}
.footer-nav{position:absolute;left:44px;top:26px;font-size:11px;color:var(--footer-text)}
.footer-nav span{margin:0 5px;color:#bbb}
.copyright{position:absolute;left:44px;top:56px;font-size:9.8px;font-weight:300;color:var(--footer-muted)}
.social{position:absolute;left:713px;top:26px;display:flex;gap:4px}
.social i{width:23px;height:23px;border-radius:4px;background:#3a8fd0;display:block}
</style>
</head>
<body>
<div class="top-band"></div>

<nav class="utility-nav">Home<span>|</span>Products<span>|</span>Services<span>|</span>Newsletter<span>|</span>Contact Us</nav>

<div class="brand"><div class="brand-mark"></div><div class="brand-name">KORVELL<br>MARINE</div></div>

<div class="search">Search here..
  <svg width="14" height="14" viewBox="0 0 14 14"><circle cx="6" cy="6" r="4.5" fill="none" stroke="#777" stroke-width="2"/><line x1="9.3" y1="9.3" x2="13" y2="13" stroke="#777" stroke-width="2.2"/></svg>
</div>

<nav class="main-nav">
  <a>Mining<br>Companies</a><a>Tailings<br>Dams</a><a>Rivers</a><a>Creeks</a><a>Dams</a><a>Marinas</a><a>Industrial<br>Ponds</a><a>Civil<br>Works</a><a>Aquatic Weed<br>Removal</a><a>Dredge Slurry<br>Separation Systems</a><a>De watering<br>Geo Textile Bags</a>
</nav>

<section class="hero">
  <div class="hero-photo" role="img" aria-label="Green amphibious walking excavator dredge being lifted by crane under a blue sky">
    <svg class="hero-arrows" width="30" height="18" viewBox="0 0 30 18"><path d="M11 2 4 9l7 7M19 2l7 7-7 7" fill="none" stroke="#fff" stroke-width="2.5"/></svg>
  </div>
</section>

<div class="card-arrow" style="left:30px"><svg width="10" height="12"><path d="M7 1 2 6l5 5" fill="none" stroke="#4a7890" stroke-width="2"/></svg></div>
<div class="card-arrow" style="left:792px"><svg width="10" height="12"><path d="M3 1l5 5-5 5" fill="none" stroke="#4a7890" stroke-width="2"/></svg></div>

<article class="card" style="left:64px">
  <div class="card-photo" role="img" aria-label="Amphibious dredge loaded on a truck trailer" style="background:linear-gradient(#9ab6c4,#4f7a4a 60%,#7a7368)"></div>
  <h3>Tailings Dams</h3><p>Curabitur vel mi sit amet magna malesuada ultrices.</p>
</article>
<article class="card" style="left:246px">
  <div class="card-photo" role="img" aria-label="Amphibious dredge lifted by crane" style="background:linear-gradient(#5e9ddf,#8fbde6 50%,#3f7a48)"></div>
  <h3>River Creeeks &amp; Ponds</h3><p>Curabitur vel mi sit amet magna malesuada ultrices.</p>
</article>
<article class="card" style="left:428px">
  <div class="card-photo" role="img" aria-label="Amphibious excavator working on a sandy beach" style="background:linear-gradient(#6aa6e2,#a7c9e0 50%,#c9b894)"></div>
  <h3>Flood Controls</h3><p>Curabitur vel mi sit amet magna malesuada ultrices.</p>
</article>
<article class="card" style="left:610px">
  <div class="card-photo" role="img" aria-label="Dredge with weed rake clearing a waterway" style="background:linear-gradient(#3f5a3a,#6c8d5a 50%,#5a6b66)"></div>
  <h3>Cleaning Up Waterways</h3><p>Curabitur vel mi sit amet magna malesuada ultrices.</p>
</article>

<section class="why">
  <h2>Why Pick Us?</h2>
  <p class="lead">Korvell Marine has been working as waterways engineers since 1995.</p>
  <p class="body">Our amphibious dredges are highly mobile and is easily transported by truck to anywhere in Australia. Our portable dewatering systems enable us to pump straight from the dregde and dry material down to 25 microns. We are able to dredge small ponds or marinas&nbsp; to mine sludge or industrial dewatering projects.</p>
  <ul class="checklist">
    <li><svg width="11" height="9"><path d="M1 5l3 3 6-7" fill="none" stroke="#1a8f8c" stroke-width="2.2"/></svg>Suction and backhoe dredging in rivers, canals, harbours, lakes and coastal waters.</li>
    <li><svg width="11" height="9"><path d="M1 5l3 3 6-7" fill="none" stroke="#1a8f8c" stroke-width="2.2"/></svg>Amphibious Dredging in areas where it is difficult or impossible to work with other machinery (wetlands, shallow waters, shorelines, industrial pools, under bridges, in tunnels, etc).</li>
    <li><svg width="11" height="9"><path d="M1 5l3 3 6-7" fill="none" stroke="#1a8f8c" stroke-width="2.2"/></svg>Where a versatile dredger is needed, which can both pump and excavate.</li>
    <li><svg width="11" height="9"><path d="M1 5l3 3 6-7" fill="none" stroke="#1a8f8c" stroke-width="2.2"/></svg>Where it is not feasible to mobilise several single-purpose machines (cutter-suction dredger, ba3ckhoe dredger, tugboat, assembly cranes).</li>
    <li><svg width="11" height="9"><path d="M1 5l3 3 6-7" fill="none" stroke="#1a8f8c" stroke-width="2.2"/></svg>Where pile driving in water or on the shoreline is needed.</li>
    <li><svg width="11" height="9"><path d="M1 5l3 3 6-7" fill="none" stroke="#1a8f8c" stroke-width="2.2"/></svg>Where vegetation disturbs conventional dredgers.</li>
  </ul>
</section>

<aside class="gallery">
  <div class="gallery-head">Photo Gallery</div>
  <div class="thumb" role="img" aria-label="Dredge on truck" style="left:15px;top:57px;background:linear-gradient(#8aa5a8,#4e6e4a)"></div>
  <div class="thumb" role="img" aria-label="Green dredge arm" style="left:94px;top:57px;background:linear-gradient(#5f9ad8,#3d8048)"></div>
  <div class="thumb" role="img" aria-label="Excavator bucket close-up" style="left:172px;top:57px;background:linear-gradient(#7b8a86,#4a4a40)"></div>
  <div class="thumb" role="img" aria-label="Dewatered material pile" style="left:15px;top:131px;background:linear-gradient(#9aa2a6,#8b7e6c)"></div>
  <div class="thumb" role="img" aria-label="Dredge cabin interior" style="left:94px;top:131px;background:linear-gradient(#d8dcdc,#8f9693)"></div>
  <div class="thumb" role="img" aria-label="Dredge on water" style="left:172px;top:131px;background:linear-gradient(#49606a,#2f4a3a)"></div>
  <div class="thumb" role="img" aria-label="Dredge floating at a jetty" style="left:15px;top:205px;background:linear-gradient(#b5c6cf,#3a5648)"></div>
  <div class="thumb" role="img" aria-label="Dredge among trees" style="left:94px;top:205px;background:linear-gradient(#91a77f,#3f6a3a)"></div>
  <div class="thumb" role="img" aria-label="Dredge in grass" style="left:172px;top:205px;background:linear-gradient(#7fa36a,#2f6d3e)"></div>
  <div class="btn">View More Gallery</div>
</aside>

<footer class="footer">
  <nav class="footer-nav">Home<span>|</span>Quotation<span>|</span>About<span>|</span>Services<span>|</span>Gallery<span>|</span>Flood Control<span>|</span>Mobility<span>|</span>Cutter Suction<span>|</span>Support<span>|</span>Contact Us</nav>
  <p class="copyright">© 2013 Company Name.&nbsp; All right reseved.&nbsp; Term of Use</p>
  <div class="social"><i></i><i></i><i></i><i></i></div>
</footer>
</body>
</html>
```